i would like a business card to leave with customers and potential customers for electrical work and for the supply and install of reverse cycle airconditioning in the domestic and commercial market.
I own my own business and im a sole trader. I have an a'class electrical lisence and also a refrigeration lisence so i am
able to offer complete installations in airconditioning by a fully qualified and lisenced tradesman.
im looking for something that comes across as unique and professional.
i had the coluor black and some gold in mind but open to any coluors.
something like Beacon Electrical & Refrigeration
or Beacon Air.
i will use this design on a business card to advertise through summer to help generate installs through the busy season.

Target Market(s)

Mainly domestic house holds through summer who are in need of airconditioning and reliable information to acomadate thier cooling and heating requirements

Industry/Entity Type

Electrical

Requirements
Must have
• Business name- Beacon
My name- Peter Wollaston
My mobile no- 0457 819 302
My email- prwollaston@tarvel.com.au
Installation & Decomissioning of aiconditioning split systems
LIC NO: KTR 407516
Nice to have
• Beacon Electrical & Refrigeration

```html
<!DOCTYPE html>
<html lang="en">
<head>
<meta charset="utf-8">
<title>Beacon Electrical &amp; Refrigeration – Business Card</title>
<link rel="stylesheet" href="https://fonts.googleapis.com/css2?family=Source+Sans+3:wght@300;400&display=swap">
<style>
  :root {
    --backdrop: #000000;
    --card-white: #ffffff;
    --navy: #1f3a94;
    --blue: #0565c4;
    --cyan: #12b4ee;
    --text-light: #ffffff;
    --text-soft: #cfe8fb;
    --text-grey: #555a60;
  }
  * { margin: 0; padding: 0; box-sizing: border-box; }
  html, body {
    width: 1200px;
    height: 1173px;
    overflow: hidden;
    background: var(--backdrop);
  }
  .canvas {
    position: relative;
    width: 1200px;
    height: 1173px;
    font-family: "Source Sans 3", "Myriad Pro", sans-serif;
  }
  .card {
    position: absolute;
    width: 691px;
    height: 397px;
    border-radius: 27px;
    overflow: hidden;
  }
  .card--front {
    left: 244px;
    top: 144px;
    background: linear-gradient(160deg, var(--navy) 0%, var(--blue) 45%, var(--cyan) 100%);
    color: var(--text-light);
  }
  .owner-name {
    position: absolute;
    left: 0;
    right: 0;
    top: 170px;
    text-align: center;
    font-weight: 300;
    font-size: 42px;
    letter-spacing: 0.2px;
  }
  .owner-role {
    position: absolute;
    right: 209px;
    top: 222px;
    font-weight: 300;
    font-size: 24px;
    color: var(--text-soft);
  }
  .service-lines {
    position: absolute;
    left: 0;
    right: 0;
    top: 330px;
    text-align: center;
    font-weight: 300;
    font-size: 17px;
    line-height: 26px;
  }
  .card--back {
    left: 247px;
    top: 574px;
    background: var(--card-white);
  }
  .name-band {
    position: absolute;
    left: 0;
    top: 60px;
    width: 599px;
    height: 106px;
    background: linear-gradient(90deg, var(--navy) 0%, var(--blue) 40%, var(--cyan) 100%);
    display: flex;
    align-items: center;
    padding-left: 32px;
    color: var(--text-light);
    font-weight: 400;
    font-size: 33px;
  }
  .contact-list {
    position: absolute;
    right: 17px;
    top: 226px;
    list-style: none;
    text-align: right;
    color: var(--text-grey);
    font-weight: 300;
    font-size: 20px;
    line-height: 30px;
  }
</style>
</head>
<body>
<div class="canvas">
  <section class="card card--front">
    <h1 class="owner-name">Peter Wollaston</h1>
    <p class="owner-role">CEO</p>
    <p class="service-lines">Installation &amp; Decomissioning of aiconditioning split systems<br>LIC NO: KTR 407516</p>
  </section>

  <section class="card card--back">
    <div class="name-band">Beacon Electrical &amp; Refrigeration</div>
    <ul class="contact-list">
      <li>0457 819 302</li>
      <li>prwollaston@tarvel.com.au</li>
      <li>chirpline.com/peter</li>
      <li>friendwall.com/peter</li>
      <li>workweb.com/in/peter</li>
    </ul>
  </section>
</div>
</body>
</html>
```